Titans of Dirt Z event poster / flyer

Looking for an event flyer designed.
Looking for a 1987 theme for a 2 stroke motocross race. Would like to copy the 1987 giants of sound flyer.
On the poster where it says 1987 putting a slash through it. And putting our date of June 7th - june 9 th. 2024 on it .
Schedule will be
Friday june 7th, 2 stroke practice
Show and shine Friday after practice (bike show)
Also, would like to promote a live 80s band Friday night.
titans of dirt z race Saturday june 8th
(2 stroke only.)
2 stroke straight rhythm event Saturday night under the lights.
Sunday KTV june 9th
2 stroke and 4 stroke race.
On part of the flyer, I would like to use this copper falcon image, holding some balls of steel. One idea do you have balls of steel?
Our premier class will be themed the storm runner 500 two-stroke big bore class. We Would like to advertise that all who dare race a big bore 2 stroke are sponsored. No race fee for this class.
Trophy & Awards podium celebration, Saturday after the event.
$5,000 added pro purse plus 100% payback
For 125cc and 250cc pro classes
Website www.titansofdirtz-example.com
Images the Varela with number six on it would be a good advertisement for the show and shine.
I think the number 98 going through the turn on the green bike would be great to add as a photo on the flyer.
Motocross

```html
<!DOCTYPE html>
<html lang="en">
<head>
<meta charset="utf-8">
<title>Titans of Dirt Z – 2 Stroke Straight Rhythm Event</title>
<link rel="stylesheet" href="https://fonts.googleapis.com/css2?family=Saira+Expanded:wght@700;800&family=Saira+Semi+Expanded:wght@600;700&display=swap">
<style>
  :root {
    --page: #ffffff;
    --red-hot: #d2341d;
    --red-deep: #7c1c10;
    --band-black: #1b1b1b;
    --grass-red: #e0391f;
    --text-white: #ffffff;
    --money-yellow: #ffe21a;
    --logo-ring: #bdbdbd;
  }
  * { box-sizing: border-box; margin: 0; padding: 0; }
  html, body {
    width: 1200px; height: 1200px; overflow: hidden;
    background: var(--page);
  }
  .poster {
    position: absolute; left: 231px; top: 78px;
    width: 738px; height: 1044px;
    overflow: hidden;
    color: var(--text-white);
    font-family: "Saira Semi Expanded", sans-serif;
    box-shadow: 0 0 40px rgba(0,0,0,0.12);
  }
  .poster-art { position: absolute; inset: 0; width: 100%; height: 100%; }

  .band-logo {
    position: absolute; left: 246px; top: 27px;
    width: 242px; height: 242px; border-radius: 50%;
    background: #000; border: 2px solid var(--logo-ring);
    display: flex; align-items: center; justify-content: center;
    text-align: center;
    font-family: "Saira Semi Expanded", sans-serif; font-weight: 700;
    font-size: 24px; line-height: 1.25; letter-spacing: 1px;
  }

  .line {
    position: absolute; left: 50%;
    white-space: nowrap; line-height: 1; text-align: center;
    transform: translate(-50%, -50%);
  }
  .headline-line {
    font-family: "Saira Expanded", sans-serif; font-weight: 800;
    transform: translate(-50%, -50%) rotate(-8deg);
  }
  .headline-main { font-size: 68px; }
  .headline-sub { font-size: 31px; }
  .headline-note { font-size: 21px; }

  .day { font-size: 27px; font-weight: 700; }
  .race { font-size: 19px; font-weight: 700; }
  .purse-amount {
    font-family: "Saira Expanded", sans-serif;
    font-size: 50px; font-weight: 800; color: var(--money-yellow); letter-spacing: 1px;
  }
  .purse-note { font-size: 19px; font-weight: 700; }
  .website { font-size: 18px; font-weight: 600; letter-spacing: 5px; }
</style>
</head>
<body>
<main class="poster">
  <svg class="poster-art" viewBox="0 0 590 835" preserveAspectRatio="none">
    <defs>
      <linearGradient id="photoTone" x1="0" y1="0" x2="0.4" y2="1">
        <stop offset="0" stop-color="#b52a18"/>
        <stop offset="0.35" stop-color="#d2341d"/>
        <stop offset="0.6" stop-color="#7c1c10"/>
        <stop offset="0.82" stop-color="#3a1c12"/>
        <stop offset="1" stop-color="#6e5a10"/>
      </linearGradient>
      <linearGradient id="grassTone" x1="0" y1="0" x2="0" y2="1">
        <stop offset="0" stop-color="#e6c81c"/>
        <stop offset="1" stop-color="#a58f16"/>
      </linearGradient>
    </defs>
    <rect class="bike-photo" width="590" height="835" fill="url(#photoTone)" role="img" aria-label="Red-toned photo of a vintage two-stroke motocross bike parked in a workshop"/>
    <polygon class="grass-red" fill="var(--grass-red)" points="0,250 10,226 12,262 26,232 28,272 44,244 44,286 62,258 60,300 80,276 76,320 0,330"/>
    <polygon class="grass-yellow" fill="url(#grassTone)" points="0,770 12,730 22,760 34,712 46,756 60,722 72,752 84,702 96,748 110,716 122,746 136,696 148,744 162,710 176,738 190,688 204,736 218,704 232,732 248,682 262,730 276,698 290,724 306,676 320,722 334,692 348,718 364,670 378,714 392,686 406,712 422,664 436,708 450,680 464,706 480,658 494,702 508,674 522,700 538,650 552,696 566,668 578,692 590,646 590,835 0,835"/>
    <polygon class="title-band" fill="var(--band-black)" opacity="0.94" points="0,240 12,214 24,238 38,202 50,232 64,196 76,228 92,188 104,222 120,184 132,216 148,178 160,210 176,172 188,206 204,168 216,200 232,164 244,196 260,158 272,190 288,154 300,186 316,150 328,182 344,146 356,178 372,142 384,174 400,138 412,170 428,134 440,166 456,130 468,162 484,126 496,158 512,122 524,154 540,118 552,150 568,114 578,144 590,110 590,392 578,418 566,386 552,424 540,392 524,432 512,398 496,438 484,404 468,444 456,410 440,452 428,416 412,458 400,422 384,466 372,428 356,472 344,434 328,478 316,440 300,484 288,446 272,490 260,452 244,496 232,458 216,502 204,464 188,508 176,470 160,514 148,476 132,520 120,482 104,526 92,488 76,532 64,494 48,538 36,500 20,544 10,506 0,520"/>
  </svg>

  <div class="band-logo">COPPER<br>FALCON</div>

  <header class="headline">
    <h1 class="line headline-line headline-main" style="top:362px">2 STROKE</h1>
    <p class="line headline-line headline-sub" style="top:423px">STRAIGHT RHYTHM EVENT</p>
    <p class="line headline-line headline-note" style="top:462px">SATURDAY NIGHT UNDER THE LIGHTS</p>
  </header>

  <section class="details">
    <p class="line day" style="top:553px">Sunday</p>
    <p class="line day" style="top:598px">KTV june 9th</p>
    <p class="line race" style="top:667px">2 stroke and 4 stroke race</p>
    <p class="line race" style="top:712px">Trophy &amp; Awards podium celebration,</p>
    <p class="line race" style="top:744px">Saturday after the event</p>
    <p class="line purse-amount" style="top:814px">$5,000</p>
    <p class="line purse-note" style="top:860px">added pro purse plus</p>
    <p class="line purse-note" style="top:889px">100% payback</p>
    <p class="line purse-note" style="top:928px">125cc and 250cc pro classes</p>
    <p class="line website" style="top:985px">www.titansofdirtz-example.com</p>
  </section>
</main>
</body>
</html>
```